Up to the Challenge? Canadian based consulting company needs a two sided business card design

A Canadian based security risk management consulting company needs a two-sided business card design. What we do is provide advice and guidance related to emergency, security and business continuity management for small, medium and large companies to help ensure the protection of their people, assets, information, services, operations and reputation.

The final design should be simple, only one or two colours, eye catching, professional and one that makes people look at three or more times just because it looks so darn good.

I have include examples of business cards I like.

Target Market(s)

Small, medium and large companies.

Industry/Entity Type

Security

Contact Information for Business Card

Business Card Size: Standard size of 3.5" (89mm) x 2.0" (51mm) - (see full specifications and guides on PRINTLY's website if required)
Card Stock: Looking to use PRINTLY's Velm 32pt stock textured paper - seam colour either chili red or black
Business Name: The Harrowgate Partners
Website: www.theharrowgatepartners.example
Telephone: (555)310-2968
Name: Dana Ostrander
Position: Principle
e-mail: Dana.Ostrander@theharrowgatepartners.example

Font styles to use
Serif

Colors
ec1f27
000000
9d9d9d
aaaaaa
606060

Requirements
Must have
• - "The Harrowgate Partners" logo (see uploaded files). I have included grey scale and colour versions.
• - Business card details (as above)
Nice to have
• - One side black or grey scale.
• - Other side would likely be white.
• - Everyone likes the silver logo on the black background.
• - Small element of colour i.e. red but I'm leaning more to greyscale.
Should not have
• - A lot of colour. Keep it simple.

```html
<!DOCTYPE html>
<html lang="en">
<head>
<meta charset="utf-8">
<title>The Harrowgate Partners – Business Card</title>
<link href="https://fonts.googleapis.com/css2?family=Cinzel:wght@400;600&family=EB+Garamond:wght@400&display=swap" rel="stylesheet">
<style>
  :root {
    --backdrop: #3a3a3a;
    --card-dark: #1c1b22;
    --card-light: #e6e6e8;
    --silver: #f2f2f2;
    --silver-muted: #9d9d9d;
    --logo-grey: #606060;
  }
  * { box-sizing: border-box; margin: 0; padding: 0; }
  html, body {
    width: 1200px; height: 799px; overflow: hidden;
    background: var(--backdrop);
  }
  .stage {
    width: 1200px; height: 799px;
    display: flex; align-items: center; justify-content: center; gap: 40px;
  }
  .card {
    width: 540px; height: 309px;
    display: flex; flex-direction: column; align-items: center; justify-content: center;
    box-shadow: 0 10px 30px rgba(0,0,0,0.45);
  }
  .card--back {
    background: var(--card-dark);
    color: var(--silver);
    font-family: "EB Garamond", serif;
    text-align: center;
  }
  .brand-mark {
    display: flex; align-items: center; gap: 10px;
    margin-bottom: 12px;
  }
  .brand-mark__dot {
    width: 30px; height: 30px; border-radius: 50%;
    background: var(--silver);
  }
  .brand-mark__name {
    font-family: "Cinzel", serif; font-weight: 400;
    font-size: 13px; letter-spacing: 2px; color: var(--silver);
    text-transform: uppercase;
  }
  .divider {
    width: 210px; height: 1px; background: var(--silver-muted);
    margin-bottom: 10px;
  }
  .person-name {
    font-family: "Cinzel", serif; font-weight: 400;
    font-size: 24px; letter-spacing: 1.5px; text-transform: uppercase;
    margin-bottom: 4px;
  }
  .person-role { font-size: 16px; margin-bottom: 10px; }
  .contact-line { font-size: 14px; line-height: 1.35; }

  .card--front { background: var(--card-light); }
  .front-logo {
    display: flex; align-items: center; gap: 22px;
  }
  .front-logo__square {
    width: 54px; height: 54px; background: var(--logo-grey);
  }
  .front-logo__wordmark {
    font-family: "Cinzel", serif; font-weight: 600;
    color: var(--logo-grey); text-transform: uppercase; text-align: center;
    line-height: 1.1;
  }
  .front-logo__line1 { display: block; font-size: 28px; letter-spacing: 1px; }
  .front-logo__line2 { display: block; font-size: 18px; letter-spacing: 5px; }
</style>
</head>
<body>
  <main class="stage">
    <section class="card card--back">
      <div class="brand-mark">
        <span class="brand-mark__dot"></span>
        <span class="brand-mark__name">The Harrowgate Partners</span>
      </div>
      <div class="divider"></div>
      <h1 class="person-name">Dana Ostrander</h1>
      <p class="person-role">Principle</p>
      <p class="contact-line">(555)310-2968</p>
      <p class="contact-line">Dana.Ostrander@theharrowgatepartners.example</p>
      <p class="contact-line">www.theharrowgatepartners.example</p>
    </section>

    <section class="card card--front">
      <div class="front-logo">
        <span class="front-logo__wordmark">
          <span class="front-logo__line1">The Harrowgate</span>
          <span class="front-logo__line2">Partners</span>
        </span>
        <span class="front-logo__square"></span>
      </div>
    </section>
  </main>
</body>
</html>
```